Wedding design templates - fresh

We require 3 different wedding designs. I have attached the watercolour images for the graphic designer to use on each template. I want to be able to easily change the name and location of the invitation when needed and be able to freely use whatever font is used, so that the invite becomes our template. I want something fresh with a modern layout but on a white background. The use of coloured fonts are okay to suit the images provided. The size of the card stock is A5 (half of an A4) please consider bleeds etc for printing.

Target Market(s)

Bridal market - young couples

Industry/Entity Type

Wedding

Font styles to use
Serif
Sans Serif
Script

Requirements
Must have
• Be able to use fonts and change details easily. common colours that can easily fit in with a brides colour scheme. must have all details for wedding invites ie church name address etc can be any church or reception place in sydney
Nice to have
• i have uploaded some example images as to style i am looking for.
• I want to be able to run a theme with these images eg. rsvp cards, place cards etc

```html
<!DOCTYPE html>
<html lang="en">
<head>
<meta charset="utf-8">
<title>Wedding Invitation</title>
<link rel="stylesheet" href="https://fonts.googleapis.com/css2?family=Allura&family=Josefin+Sans:wght@300;400&display=swap">
<style>
  :root {
    --paper: #fcfcfc;
    --band: #e2eaea;
    --rose: #c8628d;
    --ink: #4b4646;
    --leaf-dark: #6f7f6c;
    --leaf-light: #a9bd98;
    --bloom: #efb9c6;
  }
  * { margin: 0; padding: 0; box-sizing: border-box; }
  html, body {
    width: 1200px;
    height: 848px;
    overflow: hidden;
    background: var(--paper);
  }
  .invitation {
    position: relative;
    width: 1200px;
    height: 848px;
    background: var(--paper);
    overflow: hidden;
  }
  .side-band {
    position: absolute;
    top: 0;
    height: 848px;
    background: var(--band);
  }
  .side-band--left { left: 84px; width: 130px; }
  .side-band--right { left: 994px; width: 122px; }

  .floral {
    position: absolute;
    top: 0;
    width: 300px;
    height: 848px;
  }
  .floral--left { left: 0; }
  .floral--right { left: 900px; }

  .wording {
    position: absolute;
    left: 300px;
    width: 600px;
    top: 0;
    height: 848px;
    text-align: center;
    color: var(--ink);
    font-family: "Josefin Sans", sans-serif;
    font-weight: 300;
    font-variant: small-caps;
  }
  .line {
    position: absolute;
    left: 0;
    width: 100%;
    white-space: nowrap;
    line-height: 1;
  }
  .intro { top: 116px; font-size: 32px; letter-spacing: 1.5px; }
  .couple {
    top: 180px;
    font-family: "Allura", cursive;
    font-variant: normal;
    font-weight: 400;
    font-size: 84px;
    color: var(--rose);
    letter-spacing: 3px;
  }
  .invite { top: 289px; font-size: 26px; letter-spacing: 1.2px; }
  .date-line { font-size: 29px; letter-spacing: 1.2px; }
  .date-line--day { top: 355px; }
  .date-line--year { top: 395px; }
  .date-line--time { top: 435px; }
  .venue-name {
    top: 521px;
    font-family: "Allura", cursive;
    font-variant: normal;
    font-weight: 400;
    font-size: 62px;
    color: var(--rose);
    letter-spacing: 2px;
  }
  .venue-address { top: 597px; font-size: 29px; letter-spacing: 1px; }
  .reception-label {
    top: 691px;
    font-family: "Allura", cursive;
    font-variant: normal;
    font-weight: 400;
    font-size: 70px;
    color: var(--rose);
    letter-spacing: 2px;
  }
  .reception-address { top: 768px; font-size: 27px; letter-spacing: 0.6px; }
</style>
</head>
<body>
<main class="invitation">
  <div class="side-band side-band--left"></div>
  <div class="side-band side-band--right"></div>

  <svg class="floral floral--left" role="img" aria-label="Watercolour bouquet of pink blossoms, eucalyptus leaves and baby's breath rising up the left edge" viewBox="0 0 300 848" preserveAspectRatio="none">
    <defs>
      <linearGradient id="floralLeft" x1="0" y1="0" x2="1" y2="1">
        <stop offset="0" stop-color="#a9bd98" stop-opacity="0.55"/>
        <stop offset="0.45" stop-color="#efb9c6" stop-opacity="0.45"/>
        <stop offset="0.75" stop-color="#8e9f88" stop-opacity="0.5"/>
        <stop offset="1" stop-color="#efb9c6" stop-opacity="0.5"/>
      </linearGradient>
    </defs>
    <rect x="0" y="0" width="300" height="848" fill="url(#floralLeft)"/>
  </svg>

  <svg class="floral floral--right" role="img" aria-label="Watercolour bouquet of pink blossoms, eucalyptus leaves and baby's breath rising up the right edge" viewBox="0 0 300 848" preserveAspectRatio="none">
    <defs>
      <linearGradient id="floralRight" x1="1" y1="0" x2="0" y2="1">
        <stop offset="0" stop-color="#a9bd98" stop-opacity="0.55"/>
        <stop offset="0.45" stop-color="#efb9c6" stop-opacity="0.45"/>
        <stop offset="0.75" stop-color="#8e9f88" stop-opacity="0.5"/>
        <stop offset="1" stop-color="#efb9c6" stop-opacity="0.5"/>
      </linearGradient>
    </defs>
    <rect x="0" y="0" width="300" height="848" fill="url(#floralRight)"/>
  </svg>

  <section class="wording">
    <p class="line intro">together with their families</p>
    <h1 class="line couple">Amelia &amp; Luke</h1>
    <p class="line invite">invite you to join them as they tie the knot</p>
    <p class="line date-line date-line--day">Saturday the Tenth of August,</p>
    <p class="line date-line date-line--year">two thousand fifteen</p>
    <p class="line date-line date-line--time">at Three O'clock in the Afternoon</p>
    <h2 class="line venue-name">St Aldwyn Church</h2>
    <p class="line venue-address">Elmwood Lane, Halifax, HX4 2QT</p>
    <h2 class="line reception-label">Reception to follow at</h2>
    <p class="line reception-address">The Old Mill, 18 Larkfield Street, EC2Z 7RB</p>
  </section>
</main>
</body>
</html>
```